SkyvoraQ Business Cards and Stationary Design

Need a design for our business cards and stationary. I want to carry on the theme of the logo. I want the business cards to have a design on the back. I would like the business cards and the stationary to carry the same theme, design scheme, and branding

Target Market(s)

Airlines and Maintenance Facilities

Industry/Entity Type

Aviation

Contact Information for Business Card

Name
Position Title
Address: 4827 Tollbeck Lane, Brisan Cove, Lunaria, 34951
Office Number
Mobile Number
Email
Website

Font styles to use
Serif
Sans Serif

Colors

Designer to choose colors to be used in the design.

```html
<!DOCTYPE html>
<html lang="en">
<head>
<meta charset="utf-8">
<title>SkyvoraQ Business Card</title>
<link rel="stylesheet" href="https://fonts.googleapis.com/css2?family=Cinzel:wght@500&family=Open+Sans:wght@400;600;700&display=swap">
<style>
  :root {
    --bg: #dcdcdc;
    --navy: #1b2f62;
    --navy-deep: #14244d;
    --sky: #2a9ad4;
    --ink: #17285a;
    --grey-text: #777b82;
    --grey-band: #a9abae;
    --paper: #f6f6f6;
    --white: #ffffff;
  }
  html, body {
    margin: 0;
    width: 1200px;
    height: 900px;
    overflow: hidden;
    background: var(--bg);
  }
  .canvas {
    position: relative;
    width: 1200px;
    height: 900px;
  }
  .card {
    position: absolute;
    top: 301px;
    width: 520px;
    height: 298px;
    box-shadow: 0 10px 26px rgba(0,0,0,0.18);
  }
  .card svg { display: block; width: 520px; height: 298px; }
  .card-back { left: 60px; }
  .card-front { left: 620px; }
  .serif { font-family: "Cinzel", serif; }
  .sans { font-family: "Open Sans", sans-serif; }
</style>
</head>
<body>
<main class="canvas">

  <section class="card card-back" aria-label="Card back">
    <svg viewBox="0 0 520 298" xmlns="http://www.w3.org/2000/svg">
      <defs>
        <linearGradient id="backBlue" x1="0" y1="0" x2="0" y2="1">
          <stop offset="0" stop-color="var(--sky)"/>
          <stop offset="0.55" stop-color="#1f5c98"/>
          <stop offset="1" stop-color="var(--navy)"/>
        </linearGradient>
      </defs>
      <rect class="back-paper" width="520" height="298" fill="var(--paper)"/>
      <path class="back-layer-grey" d="M360 0 C455 60 470 190 455 298 L0 298 L0 0 Z" fill="#b9bcc0"/>
      <path class="back-layer-navy" d="M345 0 C438 60 452 190 438 298 L0 298 L0 0 Z" fill="var(--navy-deep)"/>
      <path class="back-layer-mid" d="M330 0 C420 60 434 190 420 298 L0 298 L0 0 Z" fill="#223d78"/>
      <path class="back-field" d="M310 0 C400 60 414 190 400 298 L0 298 L0 0 Z" fill="url(#backBlue)"/>
      <g class="back-brand">
        <circle cx="212" cy="118" r="26" fill="none" stroke="var(--white)" stroke-width="5"/>
        <text x="212" y="180" text-anchor="middle" class="sans" font-weight="700" font-size="30" letter-spacing="6" fill="var(--white)">SKYVORAQ</text>
      </g>
      <rect class="web-plate" x="96" y="194" width="236" height="30" fill="var(--navy-deep)" opacity="0.85"/>
      <text x="214" y="215" text-anchor="middle" class="sans" font-size="15" letter-spacing="1" fill="var(--white)">www.yourwebsite.com</text>
    </svg>
  </section>

  <section class="card card-front" aria-label="Card front">
    <svg viewBox="0 0 520 298" xmlns="http://www.w3.org/2000/svg">
      <defs>
        <linearGradient id="bandBlue" x1="0" y1="0" x2="1" y2="0">
          <stop offset="0" stop-color="var(--sky)"/>
          <stop offset="1" stop-color="var(--navy)"/>
        </linearGradient>
      </defs>
      <rect class="front-paper" width="520" height="298" fill="var(--paper)"/>

      <text x="30" y="48" class="serif" font-size="25" fill="var(--ink)">Your Name</text>
      <line x1="0" y1="56" x2="172" y2="56" stroke="var(--ink)" stroke-width="1.5"/>
      <text x="84" y="80" class="sans" font-weight="600" font-size="17" fill="var(--grey-text)">Manager</text>

      <g class="contact sans" font-size="13" fill="var(--grey-text)">
        <path class="icon-phone" d="M18 106 q-3 0 -3 4 q1 7 8 9 q3 0 3 -3 l-3 -2 l-2 2 q-3 -1 -4 -4 l2 -2 Z" fill="var(--grey-text)"/>
        <text x="36" y="116">O. Number: 0 000 00 00</text>
        <rect class="icon-mobile" x="16" y="126" width="8" height="13" rx="1.5" fill="none" stroke="var(--grey-text)" stroke-width="1.5"/>
        <text x="36" y="137">M. Number: 0 000 00 00</text>
        <rect class="icon-mail" x="14" y="148" width="13" height="9" fill="none" stroke="var(--grey-text)" stroke-width="1.3"/>
        <path d="M14 148 l6.5 5 l6.5 -5" fill="none" stroke="var(--grey-text)" stroke-width="1.3"/>
        <text x="36" y="158">youremail@skyvoramail.com</text>
      </g>

      <g class="front-brand">
        <circle cx="420" cy="110" r="19" fill="none" stroke="var(--ink)" stroke-width="4"/>
        <text x="420" y="160" text-anchor="middle" class="sans" font-weight="700" font-size="21" letter-spacing="4" fill="var(--ink)">SKYVORAQ</text>
      </g>

      <path class="band-grey" d="M0 196 L388 250 C398 282 440 296 470 286 C495 278 510 256 520 242 L520 298 L0 298 Z" fill="var(--grey-band)"/>
      <path class="band-blue" d="M0 210 L384 262 C396 292 440 300 470 294 C495 289 510 268 520 256 L520 298 L0 298 Z" fill="url(#bandBlue)"/>
      <circle class="corner-seal" cx="468" cy="262" r="28" fill="var(--white)" stroke="#d3d6dc" stroke-width="3"/>
      <circle cx="468" cy="262" r="15" fill="none" stroke="#c9cde0" stroke-width="3"/>

      <g class="address" transform="rotate(7.6 20 240)">
        <path class="icon-pin" d="M22 232 a5 5 0 0 1 10 0 q0 5 -5 11 q-5 -6 -5 -11 Z" fill="var(--white)"/>
        <circle cx="27" cy="232" r="1.8" fill="var(--sky)"/>
        <text x="40" y="241" class="sans" font-size="13" fill="var(--white)">4827 Tollbeck Lane, Brisan Cove, Lunaria, 34951</text>
      </g>
    </svg>
  </section>

</main>
</body>
</html>
```